Web Design Project

We need a logo, web site and business cards for our new business, Velmora Visuals. We specialize in aerial videography and photography via drone. Currently we are mainly focusing on real estate videography but will branch into other markets and may even host training classes for flying drones.
Updates

Project Deadline Extended
Reason: The system set the deadline and it did not realize it was so short, sorry for the confusion!

Target Market(s)

Real estate agents, property managers, hotels and customers looking to learn how to fly drones.

Industry/Entity Type

Videography

Font styles to use
Sans Serif

Colors

Designer to choose colors to be used in the design.

Requirements
Must have
• Space for video feed on home page
A page for completed projects
A page for training classes
About us page

```html
<!DOCTYPE html>
<html lang="en">
<head>
<meta charset="utf-8">
<title>Velmora Visuals</title>
<link href="https://fonts.googleapis.com/css2?family=Roboto+Condensed:wght@400;700&family=Open+Sans:wght@400;600&display=swap" rel="stylesheet">
<style>
:root{
  --ink:#0d0d0d;
  --night:#111111;
  --bar:#1c1c1c;
  --paper:#ffffff;
  --orange:#f0921d;
  --grey:#8a8a8a;
  --line:#d6d6d6;
  --text:#1a1a1a;
}
*{margin:0;padding:0;box-sizing:border-box}
html,body{width:1200px;height:4000px;overflow:hidden}
body{position:relative;background:var(--paper);font-family:"Open Sans",Arial,sans-serif;color:var(--text)}
.abs{position:absolute}
.head{font-family:"Roboto Condensed","Arial Narrow",sans-serif;font-weight:700;text-transform:uppercase}

/* bands */
.band{position:absolute;left:0;width:1200px}
.band-dark{background:var(--night)}
.band-video{top:860px;height:740px;clip-path:polygon(0 80px,100% 0,100% 640px,0 100%)}
.band-projects{top:2850px;height:580px;clip-path:polygon(0 60px,100% 0,100% 500px,0 100%)}
.band-call{top:2730px;height:190px;background:var(--orange);clip-path:polygon(0 60px,100% 0,100% 130px,0 100%)}
.band-footer{top:3930px;height:70px;clip-path:polygon(0 14px,100% 0,100% 100%,0 100%)}

/* top navigation */
.topnav{top:0;left:0;width:1200px;height:72px;background:var(--ink)}
.menu{position:absolute;top:0;left:290px;display:flex;height:60px}
.menu a{display:block;padding:0 26px;line-height:60px;color:#cfcfcf;font-size:15px;text-decoration:none;font-family:"Roboto Condensed",sans-serif}
.menu a.current{background:#2c2c2c;color:#fff}
.subbar{top:96px;left:430px;width:770px;height:40px;background:var(--bar);clip-path:polygon(22px 0,100% 0,100% 100%,0 100%);display:flex;align-items:center;padding-left:40px;color:#fff;font-size:13px;font-family:"Roboto Condensed",sans-serif;font-weight:700}
.subbar .tag{background:#fff;color:var(--ink);padding:1px 6px;border-radius:8px;margin-right:14px}
.subbar .item{margin-right:26px}
.follow{position:absolute;right:20px;display:flex;align-items:center;gap:8px}
.follow .social{width:22px;height:22px;border:1px solid #777}

/* brand */
.brand{top:96px;left:40px;width:270px;height:330px;background:var(--paper);box-shadow:0 6px 18px rgba(0,0,0,.25);clip-path:polygon(0 0,100% 0,100% 88%,0 100%);display:flex;flex-direction:column;align-items:center;justify-content:center;gap:20px}
.brand .mark{width:70px;height:70px;background:var(--orange)}
.brand .name{font-family:"Roboto Condensed",sans-serif;font-weight:700;font-size:36px;line-height:38px;text-align:center;color:var(--text);letter-spacing:2px}

/* hero */
.tagline{top:420px;left:60px}
.tagline span{display:table;background:var(--ink);color:#fff;font-size:50px;line-height:60px;padding:0 8px;margin-bottom:16px}
.tagline span.accent{background:var(--orange)}
.camera{top:150px;left:560px;width:600px;height:680px;border-radius:40px;background:radial-gradient(ellipse at 55% 55%,#4a4a4a 0%,#9a9a9a 45%,#e6e6e6 75%,#fff 100%)}
.dots{top:920px;left:64px;display:flex;gap:10px}
.dots i{width:12px;height:12px;border-radius:50%;background:var(--ink)}
.dots i.on{background:var(--orange)}

/* section titles */
.section-title{left:0;width:1200px;text-align:center;font-size:60px;line-height:64px}
.lede{left:0;width:1200px;text-align:center;font-size:17px;line-height:22px}
.on-dark{color:#fff}

/* video */
.video{top:1072px;left:272px;width:660px;height:328px;background:linear-gradient(180deg,#5a7688 0%,#a8b3a6 55%,#55663f 100%);overflow:hidden}
.video .play{position:absolute;top:104px;left:290px;width:80px;height:80px;border-radius:50%;border:4px solid #fff;background:rgba(0,0,0,.25)}
.video .play:after{content:"";position:absolute;left:30px;top:22px;border-left:26px solid #fff;border-top:16px solid transparent;border-bottom:16px solid transparent}
.video .caption{position:absolute;top:208px;width:100%;text-align:center;color:#fff;font-size:44px;text-shadow:0 2px 4px #000}
.controls{position:absolute;bottom:0;left:0;width:100%;height:34px;background:#1e1e1e;display:flex;align-items:center;padding:0 12px;gap:12px;color:#ddd;font-size:12px}
.controls .progress{flex:1;height:6px;background:#555;position:relative}
.controls .progress b{position:absolute;left:0;top:0;height:6px;width:38%;background:var(--orange)}

/* timeline */
.timeline{top:1720px;left:596px;width:8px;height:960px;background:var(--line)}
.timeline-fill{top:1720px;left:596px;width:8px;height:90px;background:var(--orange)}
.node{width:22px;height:22px;border-radius:50%;background:#555;border:4px solid #fff;box-shadow:0 0 0 2px var(--line);left:589px}
.node.lead{background:var(--orange)}
.date{background:var(--ink);color:#fff;font-size:17px;padding:0 18px;line-height:34px}
.entry{width:520px}
.entry h3{font-size:22px;line-height:26px}
.entry p{font-size:13px;line-height:17px;margin-top:4px}
.entry.left{text-align:right}

/* call */
.call{top:2802px;left:180px;display:flex;align-items:center;gap:28px;color:#fff;font-size:50px;line-height:60px;white-space:nowrap;transform:rotate(-2.4deg);transform-origin:left center}
.call svg{width:76px;height:76px;flex:none}

/* projects */
.project{top:3048px;width:340px;height:240px;overflow:hidden}
.project .shot{width:100%;height:100%}
.project .label{position:absolute;bottom:14px;left:18px;right:18px;background:var(--orange);color:#fff;text-align:center;font-size:30px;line-height:44px}
.arrow{top:3152px;width:30px;height:30px;border-radius:50%;background:#fff}
.arrow svg{width:30px;height:30px}

/* training */
.course{top:3584px;width:240px;text-align:center}
.course .photo{width:232px;height:232px;border-radius:50%;margin:0 auto;border:5px solid #eee}
.course h4{font-size:22px;line-height:26px;margin-top:20px;font-weight:400}

.copyright{top:3962px;right:40px;color:#fff;font-size:12px}
.copyright b{color:var(--orange)}
</style>
</head>
<body>

<div class="band band-dark band-video"></div>
<div class="band band-dark band-projects"></div>
<div class="band band-call"></div>
<div class="band band-dark band-footer"></div>

<header class="abs topnav">
  <nav class="menu">
    <a class="current">HOME</a><a>ABOUT US</a><a>SERVICES</a><a>OUR FLEET</a><a>CONTACT</a>
  </nav>
</header>
<div class="abs subbar">
  <span class="tag">SELL</span>
  <span class="item">TOP SALES ▾</span>
  <span class="item">CATEGORIES ▾</span>
  <span class="item">LOYALTY FREE ▾</span>
  <div class="follow"><span>FOLLOW US :</span><i class="social"></i><i class="social"></i><i class="social"></i><i class="social"></i></div>
</div>

<div class="abs brand">
  <div class="mark"></div>
  <div class="name">VELMORA<br>VISUALS</div>
</div>

<h1 class="abs tagline head">
  <span>Every one is</span>
  <span>an artist!</span>
  <span class="accent">Celebrating..</span>
  <span>10 years of</span>
  <span>acomplishments</span>
</h1>
<div class="abs camera" role="img" aria-label="Photograph of a silver film camera with lens facing forward"></div>
<div class="abs dots"><i class="on"></i><i></i><i></i></div>

<h2 class="abs section-title head on-dark" style="top:946px">Video Feed</h2>
<p class="abs lede on-dark" style="top:1012px">Velmora Visuals provides everything you need to<br>ensure you have the Luxury you deserve.</p>
<div class="abs video" role="img" aria-label="Video still of hot air balloons over green hills">
  <div class="play"></div>
  <div class="caption head">10 years of sucess!</div>
  <div class="controls"><span>▶</span><span>◀))</span><div class="progress"><b></b></div><span>01:08 / 04:00</span><span>⛶</span></div>
</div>

<h2 class="abs section-title head" style="top:1556px">About Us</h2>
<p class="abs lede" style="top:1622px">Velmora Visuals provides everything you need to<br>ensure you have the Luxury you deserve.</p>

<div class="abs timeline"></div>
<div class="abs timeline-fill"></div>
<div class="abs node lead" style="top:1749px"></div>
<div class="abs node" style="top:2005px"></div>
<div class="abs node" style="top:2253px"></div>
<div class="abs node" style="top:2485px"></div>
<div class="abs node" style="top:2660px"></div>

<div class="abs date head" style="top:1743px;left:660px">October 2014</div>
<div class="abs entry" style="top:1796px;left:640px">
  <h3 class="head">Award Winner</h3>
  <p>Our aerial crew captured award winning footage of coastal estates, blending smooth drone flight paths with crisp detail. Clients praised the fast delivery, careful planning and the clear story each video told about their homes.</p>
</div>

<div class="abs date head" style="top:1999px;left:400px">February 2014</div>
<div class="abs entry left" style="top:2052px;left:40px">
  <h3 class="head">Award Winner</h3>
  <p>Our aerial crew captured award winning footage of coastal estates, blending smooth drone flight paths with crisp detail. Clients praised the fast delivery, careful planning and the clear story each video told about their homes.</p>
</div>

<div class="abs date head" style="top:2247px;left:660px">October 2014</div>
<div class="abs entry" style="top:2300px;left:640px">
  <h3 class="head">Award Winner</h3>
  <p>Our aerial crew captured award winning footage of coastal estates, blending smooth drone flight paths with crisp detail. Clients praised the fast delivery, careful planning and the clear story each video told about their homes.</p>
</div>

<div class="abs date head" style="top:2479px;left:400px">February 2014</div>
<div class="abs entry left" style="top:2532px;left:40px">
  <h3 class="head">Award Winner</h3>
  <p>Our aerial crew captured award winning footage of coastal estates, blending smooth drone flight paths with crisp detail. Clients praised the fast delivery, careful planning and the clear story each video told about their homes.</p>
</div>

<div class="abs call head">
  <svg viewBox="0 0 76 76" aria-hidden="true"><circle cx="38" cy="38" r="34" fill="none" stroke="#fff" stroke-width="4"/><path d="M27 22c3-2 5-1 6 1l3 6c1 2 0 3-1 4l-2 2c2 4 5 7 9 9l2-2c1-1 2-2 4-1l6 3c2 1 3 3 1 6l-3 3c-3 2-9 1-17-6s-10-15-8-19z" fill="#fff"/></svg>
  <span>For reservation call : 555-0198-246</span>
</div>

<h2 class="abs section-title head on-dark" style="top:2920px">Completed Projects</h2>
<p class="abs lede on-dark" style="top:2986px">Velmora Visuals provides everything you need to<br>ensure you have the Luxury you deserve.</p>

<div class="abs arrow" style="left:18px"><svg viewBox="0 0 30 30"><path d="M18 8l-7 7 7 7" fill="none" stroke="#111" stroke-width="3"/></svg></div>
<div class="abs arrow" style="left:1152px"><svg viewBox="0 0 30 30"><path d="M12 8l7 7-7 7" fill="none" stroke="#111" stroke-width="3"/></svg></div>

<div class="abs project" style="left:70px">
  <div class="shot" role="img" aria-label="Playful costume photo shoot against a pale sky" style="background:linear-gradient(160deg,#d9d9d9,#9a9a9a 60%,#5a5a5a)"></div>
  <div class="label head">Baby boy project</div>
</div>
<div class="abs project" style="left:430px">
  <div class="shot" role="img" aria-label="Aerial night view of a stadium floor" style="background:linear-gradient(160deg,#1d2c4a,#3a5680 55%,#0e1626)"></div>
  <div class="label head">Baby boy project</div>
</div>
<div class="abs project" style="left:790px">
  <div class="shot" role="img" aria-label="Black and white studio portrait session" style="background:linear-gradient(160deg,#f0f0f0,#8e8e8e 55%,#2a2a2a)"></div>
  <div class="label head">Baby boy project</div>
</div>

<h2 class="abs section-title head" style="top:3440px">Training Classes</h2>
<p class="abs lede" style="top:3506px">Velmora Visuals provides everything you need to<br>ensure you have the Luxury you deserve.</p>

<div class="abs course" style="left:200px">
  <div class="photo" role="img" aria-label="Landscape photography at dusk with a silhouetted figure" style="background:radial-gradient(circle at 50% 40%,#6a7fb0,#2a3356 70%)"></div>
  <h4 class="head">Landscape<br>Photography</h4>
</div>
<div class="abs course" style="left:480px">
  <div class="photo" role="img" aria-label="Self portrait class sample image" style="background:radial-gradient(circle at 50% 40%,#e6e6e6,#9c9c9c 70%)"></div>
  <h4 class="head">Self Portrait</h4>
</div>
<div class="abs course" style="left:760px">
  <div class="photo" role="img" aria-label="Wildlife photography in warm evening light" style="background:radial-gradient(circle at 50% 45%,#f4c06a,#b55a1e 55%,#3a1a0c)"></div>
  <h4 class="head">Wildlife<br>Photography</h4>
</div>

<div class="abs copyright">© <b>VELMORA</b> 2013-2015 ALL RIGHTS RESERVED</div>

</body>
</html>
```